Brisk Lyceum Website

We are looking for a new design of our website. The current website is www.brisklyceum-example.com. The company is the #1 pre-college math and science program in Orange County, CA. We would like to see designs that integrate our logo with a modern color scheme. We are also open for suggestions that could improve our logo. We would like a simple, minimal, clean, classy, and vibrant front-page user interface design that give the premium, modern, innovative, creative, and premier brand feel. We like the "New Retro Colors for the Web" as described here: http://www.pixelharbor-example.net/en/layout-notes-2013/.

Target Market(s)

The target market is parents with K-12 students from a diverse population. Parents are well educated with family income > $150,000. Most of the decision makers are mothers from immigrate families: 30% Chinese, 30% Korean, 15% Indian, 24% White.

Industry/Entity Type

College

Requirements
Must have
• Must read our statement of differentiation at:
• http://brisklyceum-example.com/about-us
• Your design must be reflective of your understanding of the statements.
Nice to have
• The design should also be mobil friendly.
Should not have
• While most of our current classes are math, our company is expanding to include STEM (Science, Technology, Engineering, and Math) for gifted students. Therefore, the site should not be JUST a math education site.

```html
<!DOCTYPE html>
<html lang="en">
<head>
<meta charset="utf-8">
<title>Brisk Lyceum for Gifted Youth</title>
<link rel="stylesheet" href="https://fonts.googleapis.com/css2?family=Open+Sans:wght@400;600;700&display=swap">
<style>
:root{
  --green:#4f9a2c;
  --green-dark:#3f8222;
  --green-hero:#7cc04f;
  --ink:#333;
  --muted:#666;
  --line:#ddd;
  --topbar:#2b2b2b;
  --footer:#2e2e2e;
  --footer-bottom:#1f1f1f;
  --orange:#e8643a;
  --teal:#3ebfbf;
  --amber:#f1a126;
  --rose:#d0656f;
  --link:#e08a00;
  --navy:#1f3d7a;
  --twitter:#43b5c0;
  --fb:#4a62a4;
  --rss:#ee8a1c;
  --pin:#cf3b2b;
}
*{box-sizing:border-box;margin:0;padding:0}
html,body{width:1200px;height:2691px;overflow:hidden}
body{font-family:"Open Sans",Arial,sans-serif;color:var(--ink);background:#fff;position:relative;font-size:12.5px;line-height:1.45}
a{color:var(--link);text-decoration:none}
.topbar{position:absolute;left:0;top:0;width:1200px;height:30px;background:var(--topbar)}
.topbar .util{position:absolute;right:240px;top:7px;color:#ccc;font-size:12px}
.topbar .util span{margin:0 8px}
.topbar .search{position:absolute;left:955px;top:5px;width:150px;height:20px;background:#fff;border-radius:2px;font-size:11px;color:#999;padding:2px 6px}
.topbar .search svg{position:absolute;right:5px;top:4px}
.header{position:absolute;left:0;top:30px;width:1200px;height:80px;background:#fff}
.brand{position:absolute;left:90px;top:20px;display:flex;align-items:center;gap:10px}
.brand .mark{width:40px;height:40px;border-radius:50%;background:var(--green)}
.brand .name{font-size:22px;font-weight:600;color:var(--navy);line-height:1}
.brand .name small{display:block;font-size:12px;margin-top:3px}
.nav{position:absolute;left:395px;top:34px;display:flex;font-size:13px;color:#444}
.nav span{padding:0 11px;border-right:1px solid #e5e5e5}
.nav span:last-child{border:none}
.hero{position:absolute;left:0;top:110px;width:1200px;height:318px;background:linear-gradient(90deg,#5ea83a,var(--green-hero) 55%,#6db443)}
.hero h1{position:absolute;left:225px;top:100px;color:#fff;font-size:28px;font-weight:400}
.hero p{position:absolute;left:225px;top:145px;color:#fff;font-size:15px;line-height:1.5;text-align:right;width:260px;left:170px}
.hero .dots{position:absolute;left:408px;top:198px;display:flex;gap:5px}
.hero .dots i{width:6px;height:6px;border-radius:50%;background:#fff;opacity:.8}
.hero .photo{position:absolute;left:600px;top:20px;width:395px;height:298px;background:linear-gradient(180deg,#9bcf7b,#3a4256 70%,#2c3346)}
.tiles{position:absolute;left:90px;top:428px;width:1015px;height:198px;display:flex}
.tile{flex:1;color:#fff;text-align:center;padding-top:20px}
.tile h3{font-size:17px;font-weight:400;margin:10px 0 8px}
.tile p{font-size:11.5px;line-height:1.35;padding:0 22px}
.tile.elearn{background:var(--orange)}
.tile.sched{background:var(--teal)}
.tile.news{background:var(--amber)}
.tile.reg{background:var(--rose)}
.main{position:absolute;left:90px;top:655px;width:735px}
.main h2{color:var(--green);font-size:19px;font-weight:600;margin:0 0 10px}
.main p{font-size:12.3px;line-height:1.5;margin-bottom:28px}
.why{display:flex;gap:12px}
.why .badge{flex:0 0 114px;height:92px;background:linear-gradient(180deg,#e8f2e2,#2d5aa0)}
.main h4{font-size:13px;font-weight:600;margin:-10px 0 10px}
.classes{width:735px;border-collapse:collapse;font-size:11.5px;border:1px solid #ccc}
.classes th{background:var(--green);color:#fff;text-align:left;font-weight:600;padding:9px 12px;font-size:12px}
.classes td{padding:9px 12px;vertical-align:top;line-height:1.5;border-bottom:1px solid #ddd}
.classes tr:nth-child(even) td{background:#f6f6f6}
.note{background:#f1f1ec;border:1px solid #ddd;border-top:none;padding:12px 16px;font-size:11.5px;line-height:1.55;height:232px}
.note em{color:#b58a1a}
.note .tk{color:var(--green);margin-right:6px}
.side{position:absolute;left:852px;top:653px;width:253px}
.box{border:1px solid #ddd;margin-bottom:22px}
.box-h{background:var(--green);color:#fff;font-size:16px;padding:8px 12px}
.event{display:flex;gap:8px;padding:10px}
.event .thumb{flex:0 0 72px;height:58px;background:linear-gradient(135deg,#d9d2c3,#5a6b85)}
.event p{font-size:11.5px;line-height:1.4}
.event .date{color:var(--link)}
.pager{display:flex;justify-content:space-between;border-top:1px solid #ddd;padding:4px 8px;font-size:10.5px}
.cal{border:1px solid #ccc;margin-bottom:18px}
.cal .ch{background:var(--green);color:#fff;display:flex;justify-content:space-between;padding:5px 10px;font-size:12px}
.cal table{width:100%;border-collapse:collapse;font-size:11px;text-align:center}
.cal th{font-weight:400;padding:3px 0;background:#f2f2f2}
.cal td{padding:4px 0;background:#eee;border:1px solid #fff}
.cal td.today{background:#a7d38a}
.latest h5{color:var(--green);font-size:12px;margin-bottom:6px}
.news-item{border:1px solid #ddd;border-bottom:none;padding:8px 10px;font-size:11.5px;line-height:1.35;height:78px}
.news-item:last-child{border-bottom:1px solid #ddd}
.news-item .d{color:var(--link);text-align:right;margin-top:2px}
.reg-box .lead{padding:8px 10px;font-size:11.5px;line-height:1.4}
.reg-box .lead em{color:var(--link)}
.reg-box li{list-style:none;border-top:1px solid #ddd;padding:8px 10px 8px 26px;font-size:11.5px;line-height:1.4;position:relative}
.reg-box li::before{content:"✓";position:absolute;left:10px;color:var(--green)}
.footer{position:absolute;left:0;top:2101px;width:1200px;height:478px;background:var(--footer);color:#fff}
.footer h3{position:absolute;top:34px;font-size:17px;font-weight:400}
.loc{position:absolute;top:65px;width:221px;font-size:11px;line-height:1.4;color:#ddd}
.loc .ph{height:178px;margin-bottom:8px}
.loc b{color:#fff}
.loc .maplink{display:inline-block;margin-top:20px;background:#fff;color:#c22;font-weight:700;font-size:10px;padding:2px 8px}
.related{position:absolute;left:600px;top:75px;width:225px}
.related div{border-bottom:1px solid #555;padding:10px 0;font-size:11.5px;line-height:1.4;color:#ddd;height:60px}
.follow{position:absolute;left:852px;top:75px;width:226px}
.follow div{height:72px;margin-bottom:12px;font-size:22px;line-height:1;padding:14px 16px;color:#fff;position:relative}
.follow div i{position:absolute;right:16px;top:18px;width:36px;height:36px;border-radius:50%;background:rgba(255,255,255,.35)}
.f1{background:var(--twitter)}.f2{background:var(--fb)}.f3{background:var(--rss)}.f4{background:var(--pin)}
.bottom{position:absolute;left:0;top:2579px;width:1200px;height:112px;background:var(--footer-bottom);color:#ccc;font-size:11.5px}
.bottom span{position:absolute;top:45px}
</style>
</head>
<body>
<div class="topbar">
  <div class="util">Sitemap<span>|</span>Accessibility<span>|</span>Contact</div>
  <div class="search">Search...<svg width="12" height="12" viewBox="0 0 12 12"><circle cx="5" cy="5" r="3.6" fill="none" stroke="#777" stroke-width="1.5"/><line x1="7.8" y1="7.8" x2="11" y2="11" stroke="#777" stroke-width="1.6"/></svg></div>
</div>
<header class="header">
  <div class="brand"><span class="mark"></span><div class="name">Brisk Lyceum<small>for Gifted Youth</small></div></div>
  <nav class="nav"><span>Home</span><span>About Us</span><span>Math</span><span>Physics</span><span>Chemistry</span><span>Biology</span><span>Science Fair</span><span>Fall 2013</span><span>Summer 2013</span><span>Results</span></nav>
</header>
<section class="hero">
  <h1>Welcome to our site</h1>
  <p>Math Olympiad and Problem<br>Solving Training Programs</p>
  <div class="dots"><i></i><i></i><i></i></div>
  <div class="photo" role="img" aria-label="Photo of four smiling students in school uniforms"></div>
</section>
<section class="tiles">
  <div class="tile elearn">
    <svg width="40" height="36" viewBox="0 0 40 36"><rect x="7" y="4" width="26" height="18" rx="2" fill="none" stroke="#fff" stroke-width="3"/><path d="M2 27h36l-3 5H5z" fill="#fff"/></svg>
    <h3>eLearning</h3><p>Click on eLearning to access our Online Learning Management System for current students and families.</p>
  </div>
  <div class="tile sched">
    <svg width="40" height="36" viewBox="0 0 40 36"><circle cx="20" cy="18" r="15" fill="none" stroke="#fff" stroke-width="3"/><path d="M20 9v9l7 5" fill="none" stroke="#fff" stroke-width="3"/></svg>
    <h3>Scheduler</h3><p>Click on Scheduler to make an appointment online for qualifying exams, gathering information, college counseling, or science research meetings.</p>
  </div>
  <div class="tile news">
    <svg width="40" height="36" viewBox="0 0 40 36"><rect x="5" y="3" width="30" height="30" fill="none" stroke="#fff" stroke-width="3"/><path d="M10 10h10v8H10zM23 11h8M23 16h8M10 23h21M10 28h21" stroke="#fff" stroke-width="2.5" fill="none"/></svg>
    <h3>Newsletter</h3><p>Click on Newsletter to subscribe to our monthly newsletter - The Brisk Learner.</p>
  </div>
  <div class="tile reg">
    <svg width="40" height="36" viewBox="0 0 40 36"><rect x="4" y="6" width="26" height="26" fill="none" stroke="#fff" stroke-width="3"/><path d="M10 18l6 6 18-20" fill="none" stroke="#fff" stroke-width="3.5"/></svg>
    <h3>Registration</h3><p>Click on Registration to sign up for our classes.</p>
  </div>
</section>
<main class="main">
  <h2>Math Olympiad and Problem Solving Training Programs</h2>
  <p>Welcome to Brisk Lyceum for Gifted Youth. We provide after-school enrichment programs in math, physics, chemistry, biology, and computer science, mentor middle and high school science research projects, and offer college counseling to aspiring students in pursuing their college dreams. Please explore this website to learn more about our programs and our approach to gifted education.</p>
  <h2>Why Brisk Lyceum for Gifted Youth?</h2>
  <div class="why">
    <div class="badge" role="img" aria-label="Brisk Lyceum online emblem"></div>
    <p>In 2006, Brisk Lyceum for Gifted Youth was the first academy to offer advanced math problem solving to gifted students in Orange County. With its roots in the Fairmeadow math community and locations proximate to Westbay University and Larkmoor College, Brisk Lyceum for Gifted Youth combines California Standardized Mathematics Curriculum with math competitions and problem solving to help gifted students to discover their passion, develop their skills, and fulfill their college dreams. To learn more about our philosophy, history, statement of differentiation, and approach to gifted education, <a>click here</a>.</p>
  </div>
  <h2>Brisk eLearning - A Blended Learning Platform</h2>
  <p>We are pleased to announce the launch of Brisk Lyceum eLearning Center - an online community for students and parents to learn and share knowledge. With the eLearning Center, students have access to additional learning resources, can review classroom materials, download homework solutions, view grade reports, and share knowledge and communicate with other classmates in a safe and protected environment. Parents will be able to monitor their children's learning progress and participate in forum discussions related to gifted education and math talent development. <a>Click here</a> to learn more.</p>
  <h2>2013 - 2014 School Year Classes and Registration</h2>
  <p style="margin-bottom:22px">The early registration deadline for returning students and summer camp participants is August 15. The open registration period is from August 15, 2013 - August 31, 2013. To register, click on the program title below. To learn more about class schedule, qualification, waiting list, and other information, <a>click here</a>.</p>
  <h4>Math Olympiad Classes :</h4>
  <table class="classes">
    <tr><th style="width:58px">Grade</th><th>Program Title</th><th style="width:62px">Day</th><th style="width:170px">Time</th><th style="width:95px">Location</th></tr>
    <tr><td>K</td><td>M201A - Math Olympiad Level K-1<br>M201B - Math Olympiad Level K-1</td><td>SAT<br>WED</td><td>08:45am-10:15am<br>03:45pm-05:15pm</td><td>U<br>U</td></tr>
    <tr><td>1</td><td>M201A - Math Olympiad Level K-1<br>M201B - Math Olympiad Level K-1</td><td>SAT<br>WED</td><td>08:45am-10:15am<br>03:45pm-05:15pm</td><td>U<br>U</td></tr>
    <tr><td>2</td><td>M202A - Math Olympiad Level 2<br>M202B - Math Olympiad Level 2</td><td>SAT<br>THU</td><td>10:15am-11:45am<br>03:45pm-05:15pm</td><td>U<br>U</td></tr>
    <tr><td>3</td><td>M203A - Math Olympiad Level 3<br>M203B - Math Olympiad Level 3</td><td>SAT<br>TUE</td><td>08:45am-10:15am<br>03:45pm-05:15pm</td><td>U<br>U</td></tr>
    <tr><td>4</td><td>M204A - Math Olympiad Level 4<br>M204B - Math Olympiad Level 4</td><td>SUN<br>WED</td><td>10:50am-12:20pm<br>03:45pm-05:15pm</td><td>C<br>U</td></tr>
    <tr><td>5</td><td>M205A - Math Olympiad Level 5<br>M205B - Math Olympiad Level 5 waitlist</td><td>SUN<br>THU</td><td>10:40am-12:20pm<br>03:45pm-05:15pm</td><td>C<br>U</td></tr>
    <tr><td>6</td><td>M206A - Math Olympiad Level 6 &amp; Pre-Algebra<br>M206B - Math Olympiad Level 6 &amp; Pre-Algebra<br>M206C - Math Olympiad Level 6 &amp; Pre-Algebra</td><td>SAT<br>WED<br>FRI</td><td>10:20am-12:20pm<br>05:30pm-07:30pm<br>03:45pm-05:45pm</td><td>C<br>U<br>U</td></tr>
    <tr><td>7</td><td>M207A - Math Olympiad Level 7 &amp; Algebra (AMX 8)<br>M207B - Math Olympiad Level 7 &amp; Algebra (AMX 8)</td><td>SAT<br>THU</td><td>12:30pm-02:30pm<br>05:30pm-07:30pm</td><td>C<br>U</td></tr>
    <tr><td>8</td><td>M208A - Math Olympiad Level 8 &amp; Geometry (NUMBERQUEST)<br>M208B - Math Olympiad Level 8 &amp; Geometry (NUMBERQUEST)</td><td>SAT<br>TUE</td><td>02:40pm-04:40pm<br>05:30pm-07:30pm</td><td>C<br>U</td></tr>
    <tr><td>9</td><td>M209A - Math Olympiad Level 9 &amp; Algebra II (AMX10)<br>M209B - Math Olympiad Level 9 &amp; Algebra II (AMX10)</td><td>SAT<br>FRI</td><td>04:50pm-06:50pm<br>06:00pm-08:00pm</td><td>C<br>U</td></tr>
    <tr><td>10-11</td><td>M210A - Math Olympiad Level 10 &amp; Pre-Calculus (AMX12)<br>M211A - Math Olympiad Level 11 (AIMX)<br>M212A - Math Olympiad Level 12 (JNMO/NMO)</td><td>SAT<br>SUN<br>SUN</td><td>07:00pm-09:00pm<br>07:00pm-09:00pm<br>04:50pm-06:50pm</td><td>C<br>C<br>C</td></tr>
  </table>
  <div class="note">
    <em>Location Note :</em> U - University Tower, 5120 Quarry Lane, Suite 260 ; C - Larkmoor College, GH-127<br><br>
    <em>The training programs are organized into three ten-week sessions and a Winter Bootcamp :</em><br>
    <span class="tk">✓</span>Fall Session: September 10, 2013 - November 17, 2013<br>
    <span class="tk">✓</span>Winter Session: December 3, 2013 - February 23, 2014 (Holiday Break from December 23, 2013 - January 5, 2014)<br>
    <span class="tk">✓</span>Winter Olympiads Bootcamp: December 26 - 30, 2013<br>
    <span class="tk">✓</span>Spring Session: March 3, 2014 - May 11, 2014
  </div>
</main>
<aside class="side">
  <div class="box">
    <div class="box-h">Upcoming Events</div>
    <div class="event"><div class="thumb" role="img" aria-label="Event photo of a contest session"></div><p>AMX 8<br>Write something about this program.<br><span class="date">TBD, 19-11-2013</span></p></div>
    <div class="pager"><span>&lt; Prev Events</span><span>Upcoming Events &gt;</span></div>
  </div>
  <div class="cal">
    <div class="ch"><span>&#9664;</span><span>AUGUST 2013</span><span>&#9654;</span></div>
    <table>
      <tr><th>Su</th><th>Mo</th><th>Tu</th><th>We</th><th>Th</th><th>Fr</th><th>Sa</th></tr>
      <tr><td></td><td></td><td></td><td></td><td>1</td><td>2</td><td>3</td></tr>
      <tr><td>4</td><td>5</td><td>6</td><td>7</td><td>8</td><td>9</td><td>10</td></tr>
      <tr><td>11</td><td>12</td><td class="today">13</td><td>14</td><td>15</td><td>16</td><td>17</td></tr>
      <tr><td>18</td><td>19</td><td>20</td><td>21</td><td>22</td><td>23</td><td>24</td></tr>
      <tr><td>25</td><td>26</td><td>27</td><td>28</td><td>29</td><td>30</td><td>31</td></tr>
    </table>
  </div>
  <div class="latest" style="margin-bottom:22px">
    <h5>Latest News :</h5>
    <div class="news-item">2013 College matriculation list has been published. See our notice board for further details.<div class="d">13-08-2013</div></div>
    <div class="news-item">2013 College matriculation list has been published. See our notice board for further details.<div class="d">13-08-2013</div></div>
    <div class="news-item">2013 College matriculation list has been published. See our notice board for further details.<div class="d">13-08-2013</div></div>
    <div class="news-item">2013 College matriculation list has been published. See our notice board for further details.<div class="d">13-08-2013</div></div>
    <div class="news-item">2013 College matriculation list has been published. See our notice board for further details.<div class="d">13-08-2013</div></div>
    <div class="news-item">2013 College matriculation list has been published. See our notice board for further details.<div class="d">13-08-2013</div></div>
    <div class="news-item">2013 College matriculation list has been published. See our notice board for further details.<div class="d">13-08-2013</div></div>
    <div class="news-item">2013 College matriculation list has been published. See our notice board for further details.<div class="d">13-08-2013</div></div>
    <div class="news-item">2013 College matriculation list has been published. See our notice board for further details.<div class="d">13-08-2013</div></div>
  </div>
  <div class="box reg-box">
    <div class="box-h">New Student Registration</div>
    <div class="lead"><em>Schedule a qualifying exam :</em><br>The program is designed to challenge gifted math students. All students must take a qualifying exam except the following :</div>
    <ul>
      <li>Current Brisk Lyceum students in good standing.</li>
      <li>Students enrolled in a gifted program in your school district.</li>
      <li>Students identified as gifted by GTC, EPX, or other organizations.</li>
      <li>Students who received at least 550 on their state math exam.</li>
    </ul>
  </div>
</aside>
<footer class="footer">
  <h3 style="left:90px">Locations</h3>
  <div class="loc" style="left:90px">
    <div class="ph" role="img" aria-label="Street map with the Larkmoor College campus marked" style="background:linear-gradient(180deg,#f4f4f4,#d9d9d9)"></div>
    <b>Larkmoor College, Fairmeadow</b><br>All weekend classes meet at Larkmoor College, Fairmeadow.<br>Larkmoor College<br>1530 Larkmoor West<br>Fairmeadow, CA 90001-3203<br><br>Driving Directions to Larkmoor<br>
    <span class="maplink">MapLink</span>
  </div>
  <div class="loc" style="left:343px">
    <div class="ph" role="img" aria-label="Photo of the University Tower office building" style="background:linear-gradient(180deg,#4f7fb8,#c9d3dc 60%,#6f7a6a)"></div>
    <b>WBU University Tower, Fairmeadow</b><br>All weekday classes and meetings are held at WBU University Tower, Fairmeadow.<br>Brisk Lyceum for Gifted Youth<br>5120 Quarry Lane, Suite 260<br>Fairmeadow, CA 90001-4684<br>Phone: (555) 010-2211<br>Fax: (555) 010-0888<br>e-mail: info@brisklyceum-example.com<br><br>Directions to Brisk Lyceum, Fairmeadow<br>
    <span class="maplink" style="margin-top:10px">MapLink</span>
  </div>
  <h3 style="left:600px">Related content</h3>
  <div class="related">
    <div>2013 Math Olympiad Summer Camp for Grades 5 - 6</div>
    <div>2013 Geometry and NUMBERQUEST Bootcamp for Grades 7 - 8</div>
    <div>2013 AMX 12 Summer Bootcamp for Grades 10 - 11</div>
    <div>2013 Math Olympiad Summer Camp for Grades 3 - 4</div>
    <div>2013 Jump Start Algebra and AMX 8 Bootcamp for Grades 6 - 7</div>
    <div>2013 Math Olympiad Summer Camp for Grades 8 - 10</div>
  </div>
  <h3 style="left:852px">Follow Us</h3>
  <div class="follow">
    <div class="f1">Follow<br>us<i></i></div>
    <div class="f2">Like us<i></i></div>
    <div class="f3">Feed<br>us<i></i></div>
    <div class="f4">Pin us<i></i></div>
  </div>
</footer>
<div class="bottom">
  <span style="left:90px">Brisk Lyceum for Gifted Youth, 5120 Quarry Lane, Suite 260 Fairmeadow CA 90001, (555) 010-2211</span>
  <span style="right:95px">Copyright © 2000-2013</span>
</div>
</body>
</html>
```